Premium Personal Brand — Facebook Banner (Used Across All Platforms)

Update — Additional Color Direction
In addition to the dark charcoal/slate direction already described, I'm also interested in seeing variants with:
Dark navy blue — Deep, authoritative, intelligence-community feel. Same textured/matte treatment, not flat or bright.
Warm charcoal with steel blue accent — Keep the dark base but introduce a subtle steel blue gradient, accent line, or tonal shift. Sophisticated, modern, adds dimension without adding color noise.
Both should maintain the same premium, restrained, architectural feel described in the original brief. No bright blues, no corporate PowerPoint energy — think midnight, think depth, think weight.
Everything else in the brief remains the same.
I am building a premium personal brand as an executive advisor to founders ($5M+ revenue).
This contest is Facebook-banner–focused, but the design must represent a visual system that will be reused across:
- LinkedIn
- YouTube
I- nstagram
- X (Twitter)
- Website hero sections and other brand touchpoints
Think of the Facebook banner as the primary expression of the brand — not a one-off graphic.
This project is about discovering a high-end visual style and brand feel, not decoration.
What to design
Please submit one cohesive visual system, shown primarily as:
- Facebook banner (primary focus)
The same design language should clearly translate to all platforms listed above.
Designers are responsible for using the current recommended dimensions for each platform.
Quick clarification on background direction:
Backgrounds should have depth and texture, not flat color fields. Avoid pure white, light grey, or solid black backgrounds. Think matte, architectural materials — stone, graphite, concrete, steel — not blank canvases. Subtle tonal variation is encouraged. Obvious gradients or decorative patterns are not.
Text to use
Primary Headline:
- Your Business Is Too Valuable To Be Run On Hope.
Subheadline:
- You didn’t build a business to become its prisoner.
Name:
Paul Whitaker
The headline should be the dominant visual element.
Logo note (important)
My personal logo is currently being finalized.
For this contest:
- Use a simple “PW” monogram placeholder
- Clean, bold, geometric sans-serif
- Do not design a logo
- The winning design must allow an easy logo swap later.
Headshot note (important)
- Please do not include a headshot in the banner design.
- Most platforms display a circular profile image separately.
- The banner should stand on its own using typography, layout, and tone only.
- Design the banner assuming the profile photo will sit nearby, not inside the banner.
Style direction
The design should feel:
- Premium
- Calm
- Confident
- Restrained
- High-trust
- Dark, neutral backgrounds are preferred.
- Fewer elements are better than more.
Think:
- Owner-level advisor
- Private equity / boardroom tone
- Industrial, Modern, Minimalist, Elite, Architectural, not decorative
What to avoid
Please do not submit designs that feel:
- Promotional, hype-driven, or salesy
- Like a coach, guru, or agency
- Bright, colorful, or gradient-heavy
- Busy or over-designed
- Based on stock photos
- No motivational speaker energy.
Reaction test
- If someone sees this banner on Facebook (or later on LinkedIn, YouTube, etc.), the reaction should be:
“That person is serious. I’d trust them with important decisions.”
Final note
- I am not looking for many variations.
- I am looking for one strong visual direction you believe in.
Simple beats clever.
- Restraint beats decoration.

```html
<!DOCTYPE html>
<html lang="en">
<head>
<meta charset="utf-8">
<title>Paul Whitaker — Banner System</title>
<link href="https://fonts.googleapis.com/css2?family=Montserrat:ital,wght@0,400;0,500;0,600;0,700;0,900;1,400&display=swap" rel="stylesheet">
<style>
:root{
  --sheet:#e9e9e9;
  --label:#222;
  --navy-deep:#06124a;
  --navy-mid:#10289a;
  --navy-light:#1d3fb8;
  --white:#ffffff;
  --accent:#4a8ee0;
  --accent-text:#0b2470;
  --name-blue:#7fb3f0;
  --steel-a:#ffffff;
  --steel-b:#9ea3ad;
  --steel-c:#e9ebef;
}
*{margin:0;padding:0;box-sizing:border-box}
html,body{width:1139px;height:1200px;overflow:hidden}
body{background:var(--sheet);font-family:'Montserrat',sans-serif;position:relative}
.label{position:absolute;font-style:italic;font-weight:400;font-size:21px;color:var(--label);text-align:center;transform:translate(-50%,-50%);white-space:nowrap;line-height:1.3}
.banner{position:absolute;overflow:hidden;box-shadow:0 3px 8px rgba(0,0,0,.35);color:var(--white)}
.texture{position:absolute;inset:0;background:
  radial-gradient(ellipse at 50% 45%,var(--navy-light) 0%,var(--navy-mid) 45%,var(--navy-deep) 100%)}
.diamond{position:absolute;inset:0;width:100%;height:100%}
.ln{position:absolute;line-height:1;transform:translateY(-50%);white-space:nowrap}
.center{left:0;right:0;text-align:center}
.kicker{font-weight:500;letter-spacing:.16em}
.headline{font-weight:900;letter-spacing:-.01em;
  background:linear-gradient(180deg,var(--steel-a) 0%,var(--steel-c) 35%,var(--steel-b) 60%,var(--steel-a) 100%);
  -webkit-background-clip:text;background-clip:text;color:transparent}
.runon{font-weight:500}
.hope{display:inline-block;background:var(--accent);color:var(--accent-text);font-weight:700;padding:.08em .35em;margin-left:.25em;vertical-align:.05em;line-height:1}
.sub{font-weight:500}
.name{font-weight:500}
.name b{color:var(--name-blue);font-weight:600}
.rule{display:inline-block;height:1px;background:var(--name-blue);vertical-align:middle;margin:0 10px}
.mark{position:absolute;border-radius:50%;background:var(--white);color:var(--navy-mid);font-weight:700;display:flex;align-items:center;justify-content:center;transform:translate(-50%,-50%);letter-spacing:-.02em}
</style>
</head>
<body>

<div class="label" style="left:309px;top:218px">Facebook banner 1250 x 463 px</div>
<div class="label" style="left:790px;top:161px">Website banner 1920 x 1080 px</div>
<div class="label" style="left:348px;top:474px">Twitter banner 1500 x 500 px</div>
<div class="label" style="left:348px;top:724px">youtube banner 2560 x 423 px</div>
<div class="label" style="left:348px;top:900px">linkdin banner 1584 x 396 px</div>
<div class="label" style="left:856px;top:581px">Instragram banner<br>1080 x 1350 px</div>

<!-- Facebook -->
<section class="banner" style="left:115px;top:251px;width:390px;height:145px">
  <div class="texture" role="img" aria-label="Dark navy stone texture"></div>
  <svg class="diamond" viewBox="0 0 390 145" preserveAspectRatio="none"><polygon points="195,-40 345,72 195,185 45,72" fill="#000" opacity=".18"/></svg>
  <div class="mark" style="left:195px;top:23px;width:17px;height:17px;font-size:7px">PW</div>
  <div class="ln center kicker" style="top:47px;font-size:11px">Your Business is too</div>
  <div class="ln center headline" style="top:71px;font-size:38px">VALUABLE</div>
  <div class="ln center runon" style="top:94px;font-size:14px">To Be Run On<span class="hope">HOPE</span></div>
  <div class="ln center sub" style="top:110px;font-size:6.5px">You didn’t build a business to become its prisoner</div>
  <div class="ln center name" style="top:128px;font-size:7.5px"><span class="rule" style="width:30px"></span><b>Paul</b> Whitaker<span class="rule" style="width:30px"></span></div>
</section>

<!-- Website -->
<section class="banner" style="left:557px;top:192px;width:468px;height:263px">
  <div class="texture" role="img" aria-label="Dark navy stone texture"></div>
  <svg class="diamond" viewBox="0 0 468 263" preserveAspectRatio="none"><polygon points="234,-80 440,131 234,340 28,131" fill="#000" opacity=".18"/></svg>
  <div class="mark" style="left:234px;top:37px;width:30px;height:30px;font-size:12px">PW</div>
  <div class="ln center" style="top:80px;font-size:22px;font-weight:500">Your Business is too</div>
  <div class="ln center headline" style="top:121px;font-size:60px">VALUABLE</div>
  <div class="ln center runon" style="top:165px;font-size:21px">To Be Run On<span class="hope">HOPE</span></div>
  <div class="ln center sub" style="top:197px;font-size:13px">You didn’t build a business to become its prisoner</div>
  <div class="ln center name" style="top:228px;font-size:15px"><span class="rule" style="width:60px"></span><b>Paul</b> Whitaker<span class="rule" style="width:60px"></span></div>
</section>

<!-- Twitter -->
<section class="banner" style="left:115px;top:506px;width:468px;height:156px">
  <div class="texture" role="img" aria-label="Dark navy stone texture"></div>
  <svg class="diamond" viewBox="0 0 468 156" preserveAspectRatio="none"><polygon points="105,0 468,0 468,156 105,156 20,78" fill="#000" opacity=".15"/></svg>
  <div class="mark" style="left:94px;top:78px;width:44px;height:44px;font-size:17px">PW</div>
  <div class="ln kicker" style="left:131px;top:39px;font-size:17px">Your Business is too</div>
  <div class="ln headline" style="left:129px;top:72px;font-size:55px">VALUABLE</div>
  <div class="ln runon" style="left:131px;top:107px;font-size:21px">To Be Run On<span class="hope">HOPE</span></div>
  <div class="ln sub" style="left:131px;top:128px;font-size:7.5px">You didn’t build a business to become its prisoner</div>
  <div class="ln name" style="right:23px;top:127px;font-size:12px"><b>Paul</b> Whitaker</div>
</section>

<!-- YouTube -->
<section class="banner" style="left:115px;top:757px;width:468px;height:77px">
  <div class="texture" role="img" aria-label="Dark navy stone texture"></div>
  <svg class="diamond" viewBox="0 0 468 77" preserveAspectRatio="none"><polygon points="140,0 468,0 468,77 140,77 100,38" fill="#000" opacity=".15"/></svg>
  <div class="mark" style="left:142px;top:37px;width:27px;height:27px;font-size:10px">PW</div>
  <div class="ln kicker" style="left:163px;top:14px;font-size:10px">Your Business is too</div>
  <div class="ln headline" style="left:162px;top:34px;font-size:32px">VALUABLE</div>
  <div class="ln runon" style="left:163px;top:54px;font-size:12px">To Be Run On<span class="hope">HOPE</span></div>
  <div class="ln sub" style="left:163px;top:65px;font-size:4.5px">You didn’t build a business to become its prisoner</div>
  <div class="ln name" style="right:81px;top:65px;font-size:7px"><b>Paul</b> Whitaker</div>
</section>

<!-- LinkedIn -->
<section class="banner" style="left:115px;top:932px;width:468px;height:117px">
  <div class="texture" role="img" aria-label="Dark navy stone texture"></div>
  <svg class="diamond" viewBox="0 0 468 117" preserveAspectRatio="none"><polygon points="100,0 468,0 468,117 100,117 48,58" fill="#000" opacity=".15"/></svg>
  <div class="mark" style="left:108px;top:56px;width:36px;height:36px;font-size:14px">PW</div>
  <div class="ln kicker" style="left:138px;top:23px;font-size:16px">Your Business is too</div>
  <div class="ln headline" style="left:137px;top:50px;font-size:45px">VALUABLE</div>
  <div class="ln runon" style="left:138px;top:80px;font-size:17px">To Be Run On<span class="hope">HOPE</span></div>
  <div class="ln sub" style="left:138px;top:96px;font-size:6.5px">You didn’t build a business to become its prisoner</div>
  <div class="ln name" style="right:20px;top:94px;font-size:11px"><b>Paul</b> Whitaker</div>
</section>

<!-- Instagram -->
<section class="banner" style="left:687px;top:627px;width:337px;height:421px">
  <div class="texture" role="img" aria-label="Dark navy stone texture"></div>
  <svg class="diamond" viewBox="0 0 337 421" preserveAspectRatio="none"><polygon points="168,15 330,200 168,390 7,200" fill="#000" opacity=".18"/></svg>
  <div class="mark" style="left:168px;top:68px;width:40px;height:40px;font-size:15px">PW</div>
  <div class="ln center" style="top:122px;font-size:25px;font-weight:500">Your Business</div>
  <div class="ln center" style="top:150px;font-size:25px;font-weight:500">is too</div>
  <div class="ln center headline" style="top:187px;font-size:52px">VALUABLE</div>
  <div class="ln center runon" style="top:228px;font-size:27px">To Be Run On</div>
  <div class="ln center" style="top:264px"><span class="hope" style="font-size:25px;margin:0;padding:.15em .4em">HOPE</span></div>
  <div class="ln center sub" style="top:309px;font-size:14px">You didn’t build a business to</div>
  <div class="ln center sub" style="top:326px;font-size:14px">become its prisoner</div>
  <div class="ln center name" style="top:375px;font-size:15px"><b>Paul</b> Whitaker</div>
</section>

</body>
</html>
```